Etiketten-Design für Nahrungsergänzungsmittel
Zielgruppe
Die Firma vertreibt Nahrungsergänzungsmittel, gesunde Lebensmittel, Lifestyle und Wellnessprodukte. Dies vor allem im Fitness und Sport Bereich. Die Marke und das entsprechende Logo sollen auf eine jüngere Zielgruppe 25+ ausgerichtet sein. Personen die für Ihren Körper und Gesundheit Sport treiben und zusätzlich Unterstützung benötigen. Die Produkte werden über Pictoloop durch eine Fitnesstrainerin beworben, und hauptsächlich über Varuno vertrieben. Produkte sind z. B. Produkte zur Ausdauersteigerung, verbesserte Konzentration, Schlaf, Stressbewältigung. Protein Shakes oder Vitamine für Veganer. No gos, Diät Produkte 5kg in 3 Tagen, Potenzsteigerung, Brustvergrößerung oder ähnliches.
Aufgabenstellung
Das Etikett wird auf einen wiederverschließbaren schwarz matten Kraftpapier Beutel im Format 28x20cm aufgebracht. Der Beutel und auch das Etikett sind kompostierbar, sieht aber beides hochwertig aus. Das Produkt ist ein veganes Proteinpulver zum anrühren mit Wasser oder Milchalternative. Einen ersten Entwurf habe ich hochgeladen.

```html
<!DOCTYPE html>
<html lang="de">
<head>
<meta charset="utf-8">
<title>LIVA – Veganer Protein Shake Etikett</title>
<link rel="stylesheet" href="https://fonts.googleapis.com/css2?family=Montserrat:wght@400;500;600;700;800;900&display=swap">
<style>
  :root{
    --bg:#15aaa8;
    --pouch:#262727;
    --pouch-dark:#1d1e1e;
    --teal:#17a8a6;
    --teal-soft:#2a9f9c;
    --white:#ffffff;
    --grey:#cfd3d3;
  }
  *{box-sizing:border-box;margin:0;padding:0}
  html,body{width:1200px;height:1200px;overflow:hidden}
  body{background:var(--bg);font-family:"Montserrat",sans-serif;color:var(--white);position:relative}

  .label{position:absolute;top:240px;width:400px;height:720px;background:
    radial-gradient(ellipse at 30% 20%,#2e2f2f 0%,var(--pouch) 55%,var(--pouch-dark) 100%);
    overflow:hidden}
  .label--back{left:160px}
  .label--front{left:640px}

  /* back */
  .back-title{position:absolute;left:24px;top:84px;width:352px;font-size:8px;font-weight:700;line-height:1.45}
  .back-ingredients{position:absolute;left:24px;top:112px;width:352px;font-size:6.5px;line-height:1.45;color:var(--grey)}

  .table{position:absolute;left:24px;width:328px;border-collapse:separate;border-spacing:2px;font-size:7px;text-align:center}
  .table td,.table th{height:15px;padding:0 3px}
  .table th{background:var(--teal);font-weight:700}
  .table .teal td{background:var(--teal-soft)}
  .table .dark td{background:#2f3131}
  .nutrition{top:142px}
  .nutrition .tall td{height:34px}
  .amino{top:300px}
  .amino td{height:15px}
  .amino td.v{width:30px}
  .amino .t{background:var(--teal-soft)}
  .amino .d{background:#2f3131}

  .usage{position:absolute;left:24px;top:428px;width:150px;font-size:7.5px;line-height:1.5}
  .usage strong{font-weight:700}
  .company{position:absolute;left:24px;top:494px;width:150px;font-size:6.5px;line-height:1.55;color:var(--grey)}
  .company strong{color:var(--white);font-weight:700}
  .photo{position:absolute;left:270px;top:460px;width:80px;height:250px;
    background:linear-gradient(180deg,#3a3433 0%,#2a2525 60%,#1b1a1a 100%)}
  .social-note{position:absolute;left:178px;top:590px;width:90px;font-size:6px;line-height:1.5;color:var(--teal);text-align:right}
  .social-handle{position:absolute;left:178px;top:614px;width:90px;font-size:7px;font-weight:700;text-align:right;display:flex;justify-content:flex-end;align-items:center;gap:4px}
  .social-handle .dot{width:7px;height:7px;border-radius:50%;background:var(--white)}
  .band{position:absolute;left:0;width:100%;background:var(--teal)}
  .back-band{top:690px;height:10px}

  /* front */
  .front-band-top{top:44px;height:20px}
  .front-band-bottom{top:690px;height:14px}
  .brand{position:absolute;left:0;width:100%;top:270px;display:flex;justify-content:center;align-items:center;gap:12px}
  .brand-name{font-size:44px;font-weight:800;letter-spacing:4px}
  .brand-dot{width:14px;height:14px;border-radius:50%;background:var(--teal)}
  .product-line{position:absolute;left:0;width:100%;text-align:center;font-weight:900;line-height:1}
  .product-line--vegan{top:462px;font-size:30px;color:var(--teal)}
  .product-line--shake{top:498px;font-size:30px;color:var(--white)}
</style>
</head>
<body>

<section class="label label--back" aria-label="Rückseite Etikett">
  <p class="back-title">Getränkepulver zur Herstellung eines veganen Eiweißgetränkes mit Süßungsmittel – Geschmacksrichtung Vanille</p>
  <p class="back-ingredients">Zutaten: Eiweißmischung (93%) (Erbseneiweiß, Reiseiweiß, Hanfsamenpulver, Bio Kürbiskerneiweiß), Aroma, Verdickungsmittel: Xanthan, Kokosnussmilchpulver, Süßungsmittel: Sucralose</p>

  <table class="table nutrition">
    <tr><th>Nährwertangaben pro</th><th>100g</th><th>Portion = 30g</th></tr>
    <tr class="dark tall"><td>Energie</td><td>1.694 kJ /<br>401 kcal</td><td>508 kJ /<br>120 kcal</td></tr>
    <tr class="teal"><td>Fett</td><td>8,3 g</td><td>2,5 g</td></tr>
    <tr class="dark"><td>- davon gesättigte Fettsäuren</td><td>2,2 g</td><td>0,7 g</td></tr>
    <tr class="teal"><td>Kohlenhydrate</td><td>4,0 g</td><td>1,2 g</td></tr>
    <tr class="dark"><td>- davon Zucker</td><td>1,2 g</td><td>0,4 g</td></tr>
    <tr class="teal"><td>Ballaststoffe</td><td>4,4 g</td><td>1,3 g</td></tr>
    <tr class="dark"><td>Eiweiß</td><td>75,3 g</td><td>22,6 g</td></tr>
    <tr class="teal"><td>Salz</td><td>2,15 g</td><td>0,64 g</td></tr>
  </table>

  <table class="table amino">
    <tr><th colspan="6">Aminosäurenprofil pro 100g Eiweiß</th></tr>
    <tr><td class="d">Isoleucin</td><td class="d v">4,4 g</td><td class="d">Tryptophan</td><td class="d v">1,1 g</td><td class="d">Alanin</td><td class="t v">8,9 g</td></tr>
    <tr><td class="t">Leucin</td><td class="t v">8,4 g</td><td class="t">Valin</td><td class="t v">5,3 g</td><td class="t">Asparaginsäure</td><td class="d v">11,1 g</td></tr>
    <tr><td class="d">Lysin</td><td class="d v">6,7 g</td><td class="d">Histidin</td><td class="d v">2,5 g</td><td class="d">Glutaminsäure</td><td class="t v">17,2 g</td></tr>
    <tr><td class="t">Methionin</td><td class="t v">1,4 g</td><td class="t">Arginin</td><td class="t v">8,9 g</td><td class="t">Glycin</td><td class="d v">4,2 g</td></tr>
    <tr><td class="d">Phenylalanin</td><td class="d v">5,5 g</td><td class="d">Tyrosin</td><td class="d v">3,8 g</td><td class="d">Prolin</td><td class="t v">4,4 g</td></tr>
    <tr><td class="t">Threonin</td><td class="t v">3,7 g</td><td class="t">Cystein</td><td class="t v">1,4 g</td><td class="t">Serin</td><td class="d v">5,1 g</td></tr>
  </table>

  <p class="usage"><strong>Verzehrempfehlung:</strong> 30 g Pulver<br><strong>in 300 ml Wasser lösen;</strong><br>Das Produkt ist kühl, trocken und dunkel zu lagern.</p>

  <p class="company"><strong>LIVAWERK</strong><br>Lindenweg 12<br>70199 Musterbach<br>info@livabyliva.de<br><br>Inhalt: 600g Eiweißpulver für 20 Shakes<br>Mindestens haltbar bis Ende: 08/2023; Losnummer: 977109</p>

  <p class="social-note">Besucht uns doch auf Pictoloop<br>Liebe Grüße Liva</p>
  <p class="social-handle"><span class="dot"></span>livabyliva</p>

  <div class="photo" role="img" aria-label="Foto der Fitnesstrainerin in Sportkleidung"></div>
  <div class="band back-band"></div>
</section>

<section class="label label--front" aria-label="Vorderseite Etikett">
  <div class="band front-band-top"></div>
  <div class="brand"><span class="brand-dot"></span><span class="brand-name">LIVA</span></div>
  <p class="product-line product-line--vegan">VEGANER</p>
  <p class="product-line product-line--shake">PROTEIN SHAKE</p>
  <div class="band front-band-bottom"></div>
</section>

</body>
</html>
```